Touch screen based web site design

We have a product called vTrellis.

It is a browser based touch screen application for the apartment leasing industry . You can read more about it at http://vtrellis.korvathsoft.example.

To see how the product functions, you can check the link http://www.webvtrellis.example/vtrellis.aspx?k=demo1.

We have a need to give a new look and feel to the application. The redesign is NOT to be limited to colors and shapes, but an overhaul of the screen layout, color, font scheme to make the application flow nice and smooth. The content of the pages will remain the same.

There will be animations but that can be done by our IT team, if described in concept by the designer.

Again to reiterate, all things are up for grab, do not get influenced by the images, shapes and color used currently.

Reason: None of the design are coming even close to what I am asking for. Please see the homepage of the application at http://www.korvathsoft.example/vtrellis/images/img-screenshot-lg-01.jpg. That is what I am asking for as the first page to show the design idea.

Reason: At least the last couple of designs submitted understands it is a touch screen and the home page is not a web site home page. The reason I am still not able to select a design is that the quality of graphic design elements is sub par. For example, The treatment to the options for example are not sharp and up to mark.

Target Market(s)

Propective residents walking into a apartment leasing centers

Industry/Entity Type

Apartment

Requirements
Must have
• - Must have a design where the content, like name of the property, menu options and pictures, are dynamic. So for example, do not restrict the design in a manner that we cannot switch off an option without redesign of the page.
- Good use of icons for options
- Gives the user a calm and serene feeling while maintaining a crisp modern user interface
Nice to have
• - Design in a manner that the background can be a custom image for a specific client
- Description of animation on the screen where the images selected by the client can rotate/slide/appear/animate
Should not have
• - Boxy design
- Small options that cannot be touched by fingers
- dont plan on hover animations, will not work in touch

```html
<!DOCTYPE html>
<html lang="en">
<head>
<meta charset="utf-8">
<title>Contact</title>
<link rel="stylesheet" href="https://fonts.googleapis.com/css2?family=EB+Garamond:wght@400;500;600&family=Parisienne&family=Roboto:wght@300&family=Roboto+Condensed:wght@400&display=swap">
<style>
  :root {
    --bg-top: #fafafa;
    --bg-bottom: #e9e9e9;
    --ink: #333333;
    --ghost: #dcdcdc;
    --field-border: #d6d6d6;
    --option-top: #f0f0f0;
    --option-bottom: #cfcfcf;
    --option-border: #bdbdbd;
    --orange-deep: #f08a0a;
    --orange-text: #e8870c;
    --yellow-top: #fbe52e;
    --yellow-bottom: #f2c40f;
    --submit-text: #b3780b;
    --green-top: #a8d63a;
    --green-bottom: #86bd12;
    --blue-top: #47c2ee;
    --blue-bottom: #0a8cc7;
    --nav-label: #9a9a9a;
    --nav-label-active: #4f4f4f;
  }
  * { box-sizing: border-box; margin: 0; padding: 0; }
  html, body { width: 1200px; height: 662px; overflow: hidden; }
  body {
    position: relative;
    background: linear-gradient(180deg, var(--bg-top) 0%, var(--bg-bottom) 100%);
    font-family: "EB Garamond", Georgia, serif;
    color: var(--ink);
  }
  .tagline {
    position: absolute; left: 244px; top: 16px;
    font-family: "Parisienne", cursive; font-weight: 400;
    font-size: 28px; color: #555;
    text-shadow: 0 1px 1px rgba(255,255,255,.9);
    white-space: nowrap;
  }
  .page-title {
    position: absolute; left: 40px; top: 238px;
    font-family: "Roboto", sans-serif; font-weight: 300;
    font-size: 62px; line-height: 72px; color: var(--ghost); letter-spacing: -2.5px;
    white-space: nowrap;
  }
  .divider {
    position: absolute; left: 262px; top: 88px; width: 4px; height: 476px;
    background: linear-gradient(180deg, rgba(0,0,0,0) 0%, rgba(0,0,0,.13) 45%, rgba(0,0,0,0) 100%);
  }
  .field-label {
    position: absolute; font-size: 20px; line-height: 24px; text-align: right; color: var(--ink);
    white-space: nowrap;
  }
  .text-field {
    position: absolute; left: 469px; width: 312px; height: 25px;
    border: 1px solid var(--field-border); border-radius: 13px;
    background: linear-gradient(180deg, #f3f3f3 0%, #ffffff 100%);
    box-shadow: inset 0 1px 2px rgba(0,0,0,.08);
  }
  .option {
    position: absolute; left: 507px; width: 239px; height: 35px;
    border: 1px solid var(--option-border); border-radius: 2px;
    background: linear-gradient(180deg, var(--option-top) 0%, var(--option-bottom) 100%);
    box-shadow: 0 1px 2px rgba(0,0,0,.15);
    font-weight: 600; font-size: 20px; color: var(--orange-text);
    display: flex; align-items: center; justify-content: center;
    text-shadow: 0 1px 0 rgba(255,255,255,.8);
  }
  .option .count { font-size: 22px; margin-right: 12px; }
  .checkbox {
    position: absolute; left: 10px; top: 9px; width: 16px; height: 16px;
    background: linear-gradient(180deg, #fbb431, var(--orange-deep));
    border: 1px solid #e08a12; border-radius: 2px;
  }
  .segmented {
    position: absolute; left: 507px; top: 371px; width: 239px; height: 43px;
    display: flex; border-radius: 2px; overflow: hidden;
    box-shadow: 0 1px 2px rgba(0,0,0,.2);
  }
  .segment {
    flex: 1; display: flex; align-items: center; justify-content: center; gap: 10px;
    font-weight: 600; font-size: 20px;
  }
  .segment--active {
    background: linear-gradient(180deg, #fdb12e 0%, var(--orange-deep) 100%);
    color: #b85f06; border: 1px solid #e88a10;
  }
  .segment--idle {
    background: linear-gradient(180deg, var(--option-top) 0%, var(--option-bottom) 100%);
    color: var(--orange-text); border: 1px solid var(--option-border); border-left: none;
    text-shadow: 0 1px 0 rgba(255,255,255,.8);
  }
  .radio { width: 13px; height: 13px; border-radius: 50%; }
  .segment--active .radio { background: radial-gradient(circle at 45% 40%, #fff8d8, #f5d77a); border: 1px solid #d8891a; }
  .segment--idle .radio { background: radial-gradient(circle at 45% 40%, #f7a234, #e07808); }
  .submit {
    position: absolute; left: 507px; top: 443px; width: 239px; height: 43px;
    border: 1px solid #e3b10c; border-radius: 2px;
    background: linear-gradient(180deg, var(--yellow-top) 0%, var(--yellow-bottom) 100%);
    box-shadow: 0 1px 2px rgba(0,0,0,.18);
    font-family: inherit; font-weight: 600; font-size: 19px; color: var(--submit-text);
  }
  .mailbox-art {
    position: absolute; left: 921px; top: 33px; width: 250px; height: 246px;
    border-radius: 60px 60px 80px 40px;
    background: linear-gradient(135deg, #eadf6a 0%, #a9cf3a 40%, #2da9dc 75%, #1b88c0 100%);
    opacity: .9;
  }
  .footer-band {
    position: absolute; left: 0; top: 608px; width: 1200px; height: 54px;
    background: linear-gradient(180deg, #fdfdfd 0%, #efefef 100%);
    border-top: 1px solid #d9d9d9;
  }
  .home-button {
    position: absolute; left: 58px; top: 551px; width: 82px; height: 82px; border-radius: 50%;
    background: radial-gradient(circle at 50% 30%, var(--blue-top) 0%, #20a6dd 50%, var(--blue-bottom) 100%);
    box-shadow: 0 6px 8px rgba(0,0,0,.15);
    display: flex; align-items: center; justify-content: center;
    font-family: "Roboto Condensed", sans-serif; font-size: 21px; color: #eaf8ff;
  }
  .nav-item { position: absolute; width: 86px; text-align: center; }
  .nav-tile {
    width: 86px; height: 86px; border-radius: 4px;
    background: linear-gradient(180deg, var(--green-top) 0%, var(--green-bottom) 100%);
    box-shadow: 0 2px 3px rgba(0,0,0,.2);
    display: flex; align-items: center; justify-content: center;
  }
  .nav-label {
    position: absolute; left: -30px; width: 146px; top: 87px;
    font-family: "Roboto Condensed", sans-serif; font-size: 19px; line-height: 22px; color: var(--nav-label);
    white-space: nowrap;
  }
  .nav-item--active .nav-label { top: 102px; color: var(--nav-label-active); }
  .nav-item--active .nav-tile { box-shadow: 0 12px 10px -6px rgba(0,0,0,.25); }
  .logo-text {
    font-family: "Roboto Condensed", sans-serif; font-size: 23px; line-height: 26px; color: #f2fbe0;
  }
  .icon-fill { width: 62px; height: 62px; border-radius: 6px; background: rgba(245,252,225,.55); }
</style>
</head>
<body>
  <h1 class="tagline">Where convenience meet luxury</h1>
  <div class="page-title">Contact</div>
  <div class="divider"></div>

  <form class="contact-form">
    <label class="field-label" style="right:758px; top:99px;">Name</label>
    <div class="text-field" style="top:99px;"></div>
    <label class="field-label" style="right:758px; top:138px;">Phone</label>
    <div class="text-field" style="top:137px;"></div>
    <label class="field-label" style="right:758px; top:177px;">Email</label>
    <div class="text-field" style="top:177px;"></div>

    <div class="field-label" style="right:728px; top:222px;">I’m interested in</div>
    <div class="option" style="top:220px;"><span class="checkbox"></span><span class="count">1</span>Bedroom</div>
    <div class="option" style="top:266px;"><span class="checkbox"></span><span class="count">2</span>Bedroom</div>
    <div class="option" style="top:309px;"><span class="checkbox"></span><span class="count">3</span>Bedroom</div>

    <div class="field-label" style="right:728px; top:381px;">Contact me by</div>
    <div class="segmented">
      <div class="segment segment--active"><span class="radio"></span>Email</div>
      <div class="segment segment--idle"><span class="radio"></span>Phone</div>
    </div>

    <button class="submit" type="button">Submit</button>
  </form>

  <div class="mailbox-art" role="img" aria-label="Illustration of a blue mailbox with green and yellow envelopes"></div>

  <div class="footer-band"></div>
  <div class="home-button">HOME</div>

  <nav>
    <div class="nav-item" style="left:446px; top:548px;">
      <div class="nav-tile"><div class="icon-fill" role="img" aria-label="Community icon: group of people in a circle"></div></div>
      <div class="nav-label">Community</div>
    </div>
    <div class="nav-item" style="left:602px; top:548px;">
      <div class="nav-tile">
        <svg width="64" height="58" viewBox="0 0 64 58" fill="none" stroke="#f2fbe0" stroke-width="3" stroke-linejoin="round">
          <path d="M4 28 L18 16 L32 28 V54 H4 Z"/>
          <path d="M26 20 L42 6 L60 22 V54 H32"/>
          <rect x="12" y="38" width="10" height="16" fill="#f2fbe0" stroke="none"/>
          <rect x="40" y="28" width="8" height="8"/>
        </svg>
      </div>
      <div class="nav-label">Neighborhood</div>
    </div>
    <div class="nav-item" style="left:759px; top:548px;">
      <div class="nav-tile">
        <svg width="60" height="60" viewBox="0 0 60 60" fill="none" stroke="#f2fbe0" stroke-width="3">
          <rect x="4" y="4" width="52" height="52"/>
          <path d="M4 24 H20 M20 4 V40 M20 40 H12 M34 4 V18 H48 M34 30 V56 M34 40 H56"/>
        </svg>
      </div>
      <div class="nav-label">Floor Plans</div>
    </div>
    <div class="nav-item nav-item--active" style="left:915px; top:533px;">
      <div class="nav-tile">
        <svg width="64" height="46" viewBox="0 0 64 46">
          <rect x="2" y="2" width="60" height="42" rx="2" fill="#f6fde2"/>
          <path d="M3 4 L32 26 L61 4 M3 43 L24 22 M61 43 L40 22" fill="none" stroke="#b5dc5a" stroke-width="2"/>
        </svg>
      </div>
      <div class="nav-label">Contact</div>
    </div>
    <div class="nav-item" style="left:1072px; top:548px;">
      <div class="nav-tile"><span class="logo-text">Logo<br>Here</span></div>
      <div class="nav-label">Company</div>
    </div>
  </nav>
</body>
</html>
```